Wirenexa

I'm looking to much improve our current website wirenexa.com
Updates

Low design quality

Target Market(s)

Commercial clients (Not-Residentials)

Industry/Entity Type

Office buildings and Industrial clients

Coding

Coded - Design and coding required

Number of Pages Required

5+ page

Requirements
Must have
• Very professional structured low voltage cabling projects for Wi-Fi, Audio/Video conference rooms, Access Control systems, CCTV.

```html
<!DOCTYPE html>
<html lang="en">
<head>
<meta charset="utf-8">
<title>Wirenexa — Commercial Layout Planner &amp; Budget</title>
<link href="https://fonts.googleapis.com/css2?family=Archivo:ital,wght@0,400;0,600;0,700;1,800;1,900&family=IBM+Plex+Mono:wght@400;500;600;700&family=Cormorant+Garamond:ital@1&display=swap" rel="stylesheet">
<style>
:root{
  --red:#e31e24;
  --ink:#111111;
  --text:#333333;
  --muted:#7a7a7a;
  --line:#e2e2de;
  --page:#f3f3f1;
  --white:#ffffff;
  --tile:#f1f1ef;
  --pink:#fdf0f0;
}
*{box-sizing:border-box;margin:0;padding:0}
html,body{width:1090px;height:1200px;overflow:hidden;background:var(--white)}
body{position:relative;font-family:'IBM Plex Mono',monospace;color:var(--text)}
.mono{font-family:'IBM Plex Mono',monospace}
.abs{position:absolute}

/* header */
.site-header{position:absolute;left:0;top:0;width:1090px;height:45px;background:var(--white)}
.brand{position:absolute;left:115px;top:13px;display:flex;align-items:center;gap:5px;font-family:'Archivo',sans-serif;font-weight:700;font-size:17px;color:var(--ink);letter-spacing:-.3px}
.brand-square{width:13px;height:13px;background:var(--red)}
.main-nav{position:absolute;left:256px;top:17px;display:flex;gap:17px;font-family:'Archivo',sans-serif;font-size:8px;font-weight:600;letter-spacing:1.3px;color:#6a6a6a}
.main-nav .active{color:var(--red);border-bottom:1.5px solid var(--red);padding-bottom:4px}
.header-phone{position:absolute;left:796px;top:17px;font-size:8px;letter-spacing:.8px;color:var(--ink);display:flex;align-items:center;gap:4px}
.header-cta{position:absolute;left:894px;top:10px;width:82px;height:26px;background:var(--ink);color:#fff;font-family:'Archivo',sans-serif;font-weight:700;font-size:7.5px;letter-spacing:1px;display:flex;align-items:center;justify-content:center;gap:5px}

/* hero */
.workspace{position:absolute;left:0;top:45px;width:1090px;height:781px;background:var(--page)}
.eyebrow{position:absolute;left:446px;top:35px;width:197px;height:20px;background:#fff;border:1px solid var(--line);font-size:7px;font-weight:600;letter-spacing:1.1px;color:var(--ink);display:flex;align-items:center;justify-content:center}
.hero-title{position:absolute;left:0;top:62px;width:1090px;text-align:center;font-family:'Archivo',sans-serif;font-size:34px;color:var(--ink);letter-spacing:-.5px;font-weight:400}
.hero-title em{font-weight:900;font-style:italic;letter-spacing:-1.2px}
.hero-sub{position:absolute;left:300px;top:112px;width:490px;text-align:center;font-size:8.5px;line-height:11.5px;color:#555}

.card{position:absolute;background:var(--white);border:1px solid var(--line);box-shadow:0 1px 2px rgba(0,0,0,.04)}

/* specs */
.specs{left:91px;top:169px;width:364px;height:578px;padding:18px 17px}
.section-title{display:flex;align-items:center;gap:6px;font-size:10px;font-weight:600;letter-spacing:1.2px;color:var(--ink);padding-bottom:10px;border-bottom:1px solid var(--line)}
.section-title i{width:7px;height:7px;background:var(--red);display:block}
.field-label{font-size:7px;letter-spacing:1px;color:var(--muted);text-transform:uppercase}
.type-grid{display:grid;grid-template-columns:1fr 1fr;gap:6px;margin-top:8px}
.type-tile{height:48px;background:var(--tile);border:1px solid var(--line);display:flex;flex-direction:column;align-items:center;justify-content:center;gap:7px;font-size:6.5px;letter-spacing:.4px;color:#555}
.type-tile.selected{background:var(--pink);border-color:var(--red);color:var(--ink);font-weight:600}
.row{display:flex;justify-content:space-between;align-items:center}
.value{font-size:8px;font-weight:600;color:var(--ink);letter-spacing:.5px}
.slider{position:relative;height:8px;margin-top:12px}
.slider .track{position:absolute;left:0;right:0;top:3px;height:2px;background:#ddd}
.slider .fill{position:absolute;left:0;top:2.5px;height:3px}
.slider .knob{position:absolute;top:-1px;width:10px;height:10px;border-radius:50%}
.red .fill,.red .knob{background:var(--red)}
.dark .fill,.dark .knob{background:var(--ink)}
.node-label{font-size:7px;letter-spacing:.8px;color:#666;display:flex;align-items:center;gap:5px}
.node-label i{width:5px;height:5px;display:block}
.divider{border-top:1px solid var(--line)}
.check{display:flex;align-items:center;gap:7px;font-size:6px;font-weight:600;letter-spacing:.4px;color:var(--ink)}
.box{width:11px;height:11px;border:1px solid #999;border-radius:2px;display:flex;align-items:center;justify-content:center}
.box.on{background:var(--red);border-color:var(--red)}
.select{margin-top:6px;height:25px;border:1px solid #ccc;background:#f7f7f5;display:flex;align-items:center;justify-content:space-between;padding:0 7px 0 12px;font-size:8.5px;color:var(--ink)}

/* topology */
.topology{left:479px;top:169px;width:288px;height:317px;padding:14px}
.panel-head{display:flex;justify-content:space-between;align-items:center}
.live{font-size:6.5px;letter-spacing:.6px;color:var(--muted);display:flex;align-items:center;gap:5px}
.live i{width:4px;height:4px;border-radius:50%;background:var(--red);display:block}
.grid-tag{font-size:5.5px;border:1px solid var(--line);background:#f5f5f3;padding:4px 3px;color:#777;letter-spacing:.4px}
.plan-frame{position:relative;margin-top:12px;height:194px;background:#f0f0ee;border:1px solid var(--line);padding:22px 6px 0 6px}
.plan-area{height:148px;background:linear-gradient(135deg,#ffffff,#f8efef);border:1px dashed #bbb}
.model-tag{position:absolute;right:9px;bottom:8px;background:#f7f7f5;border:1px solid var(--line);font-size:6px;letter-spacing:1px;padding:3px 5px;color:#555}
.legend{display:grid;grid-template-columns:1fr 1fr;row-gap:10px;margin-top:12px;font-size:6px;font-weight:600;letter-spacing:.5px;color:var(--ink)}
.legend span{display:flex;align-items:center;gap:5px}
.legend i{width:6px;height:6px;display:block;flex:none}
.legend-mdf{display:flex;align-items:center;gap:7px;margin-top:11px;padding-top:2px;font-size:6px;letter-spacing:.5px;color:var(--red)}
.legend-mdf i{width:10px;height:10px;border:1px solid var(--red);display:block}

.quality{left:479px;top:504px;width:288px;height:114px;background:#f6f6f4;padding:16px 14px}
.quality h3{font-size:7px;font-weight:500;letter-spacing:1px;color:#666}
.quality p{font-family:'Archivo',sans-serif;font-size:6.2px;font-weight:600;color:#444;line-height:9.5px;margin-top:6px;text-transform:uppercase}
.quality h3+p{margin-top:8px}

/* estimate */
.estimate{left:790px;top:169px;width:208px;height:343px;padding:18px 17px}
.summary-head{font-size:8.5px;font-weight:600;letter-spacing:1.3px;color:var(--ink);padding-bottom:9px;border-bottom:1px solid var(--line)}
.kv{display:flex;justify-content:space-between;align-items:baseline}
.kv .k{font-size:6.5px;letter-spacing:.9px;color:var(--muted)}
.kv .v{font-size:10px;font-weight:500;color:var(--ink)}
.cost .k{font-size:5.5px;font-weight:600;color:var(--ink);letter-spacing:.4px}
.cost .v{font-size:6px;font-weight:600;color:var(--ink)}
.cost.fiber .k,.cost.fiber .v{color:var(--red)}
.budget{margin-top:12px;height:72px;background:#f5f5f3;border:1px solid var(--line);text-align:center;padding-top:12px}
.budget small{display:block;font-size:5.5px;letter-spacing:1px;color:#888}
.budget strong{display:block;font-size:17px;font-weight:700;color:var(--red);margin-top:4px}
.budget em{display:block;font-style:normal;font-size:5px;letter-spacing:.6px;color:#888;margin-top:4px}
.btn-primary{margin-top:17px;height:32px;background:var(--ink);color:#fff;font-size:7px;font-weight:700;letter-spacing:1px;display:flex;align-items:center;gap:9px;padding-left:8px}
.btn-outline{margin-top:6px;height:26px;border:1px solid var(--line);display:flex;align-items:center;justify-content:center;gap:6px;font-size:7px;font-weight:700;letter-spacing:1px;color:var(--ink)}

.support{left:790px;top:529px;width:208px;height:100px;padding:16px 14px}
.support h3{font-size:6.5px;font-weight:500;letter-spacing:1px;color:#777}
.support p{font-family:'Cormorant Garamond',serif;font-style:italic;font-size:8px;line-height:14px;color:#555;margin-top:9px}

/* certifications */
.certs{position:absolute;left:91px;top:872px;width:908px}
.certs h2{display:flex;align-items:center;gap:6px;font-size:8.5px;font-weight:600;letter-spacing:1.5px;color:var(--ink)}
.certs p{font-size:6.5px;letter-spacing:1px;color:var(--muted);margin-top:5px}
.badges{position:absolute;right:0;top:1px;display:flex;gap:11px}
.badge{height:22px;border:1px solid #ddd;background:#f7f7f5;display:flex;align-items:center;gap:5px;padding:0 6px;font-size:6.5px;font-weight:600;letter-spacing:.4px;color:var(--ink)}
.badge i{width:6px;height:6px;border:1.2px solid var(--red);border-radius:50%;display:block}

.footer-rule{position:absolute;left:91px;width:908px;border-top:1px solid var(--line)}
.foot-col{position:absolute;top:954px;width:210px}
.foot-col h4{font-size:7.5px;font-weight:600;letter-spacing:1.2px;color:var(--ink);padding-bottom:5px;border-bottom:1px solid var(--line)}
.foot-brand{position:absolute;left:91px;top:953px;width:86px;height:28px;background:#f1f1ef;border:1px solid var(--line);display:flex;align-items:center;gap:4px;padding-left:5px;font-family:'Archivo',sans-serif;font-weight:700;font-size:13.5px;color:var(--ink);letter-spacing:-.3px}
.foot-brand i{width:10px;height:10px;background:var(--red);display:block}
.foot-about{position:absolute;left:91px;top:992px;width:215px;font-family:'Cormorant Garamond',serif;font-style:italic;font-size:7px;line-height:12.6px;color:#777}
.anniv{position:absolute;left:91px;top:1055px;height:14px;width:165px;background:var(--ink);color:#fff;font-size:6px;font-weight:600;letter-spacing:1px;display:flex;align-items:center;justify-content:center}
.links{list-style:none;margin-top:11px}
.links li{font-size:6.5px;letter-spacing:.5px;color:#555;height:18px}
.office{margin-top:10px;font-size:6.5px;line-height:10px;color:#555}
.office b{display:block;font-size:5.5px;letter-spacing:1px;color:var(--ink);margin-bottom:4px}
.pin{display:flex;gap:5px}
.dispatch{font-size:6px;letter-spacing:1px;color:#999;margin-top:11px}
.phone-bar{margin-top:7px;height:27px;background:var(--ink);color:#fff;font-size:7px;font-weight:600;display:flex;align-items:center;gap:6px;padding-left:9px;letter-spacing:.5px}
.mail{margin-top:11px;font-size:7px;font-weight:600;color:var(--ink);text-decoration:underline;display:flex;align-items:center;gap:5px}
.social{display:flex;gap:6px;margin-top:6px}
.social span{width:23px;height:23px;border:1px solid var(--line);background:#f7f7f5;display:flex;align-items:center;justify-content:center}
.social i{width:6px;height:6px;border-radius:50%;background:#444;display:block}
.copyright{position:absolute;left:91px;top:1145px;font-size:6.5px;letter-spacing:.4px;color:#888}
.legal{position:absolute;right:91px;top:1145px;font-size:6.5px;letter-spacing:.4px;color:#888;display:flex;gap:12px}
</style>
</head>
<body>

<header class="site-header">
  <div class="brand"><span class="brand-square"></span>Wirenexa</div>
  <nav class="main-nav">
    <span>HOME</span><span>SERVICES</span><span>PORTFOLIO</span><span class="active">ESTIMATE PLANNER</span><span>MONITORING</span><span>ABOUT US</span><span>CONTACT</span>
  </nav>
  <div class="header-phone">
    <svg width="9" height="9" viewBox="0 0 24 24" fill="none" stroke="#e31e24" stroke-width="2.2"><path d="M22 16.9v3a2 2 0 0 1-2.2 2 19.8 19.8 0 0 1-8.6-3.1 19.5 19.5 0 0 1-6-6A19.8 19.8 0 0 1 2.1 4.2 2 2 0 0 1 4.1 2h3a2 2 0 0 1 2 1.7c.1.9.4 1.8.7 2.7a2 2 0 0 1-.5 2.1L8 9.8a16 16 0 0 0 6 6l1.3-1.3a2 2 0 0 1 2.1-.5c.9.3 1.8.6 2.7.7a2 2 0 0 1 1.7 2z"/></svg>
    (888) 555-0142
  </div>
  <div class="header-cta">
    <svg width="8" height="8" viewBox="0 0 24 24" fill="none" stroke="#fff" stroke-width="2.4"><rect x="3" y="4" width="18" height="18"/><path d="M3 10h18M8 2v4M16 2v4"/></svg>
    ESTIMATE
  </div>
</header>

<main class="workspace">
  <div class="eyebrow">INTERACTIVE COST &amp; BLUEPRINT ENGINE</div>
  <h1 class="hero-title">COMMERCIAL <em>LAYOUT PLANNER &amp; BUDGET</em></h1>
  <p class="hero-sub">Adjust the sliders below to match your building size and workstation details. View your network structure dynamically laid out on the interactive blueprint.</p>

  <section class="card specs">
    <div class="section-title"><i></i>1. FACILITY SPECIFICATIONS</div>

    <div class="field-label" style="margin-top:17px">Facility infrastructure type</div>
    <div class="type-grid">
      <div class="type-tile selected">
        <svg width="12" height="12" viewBox="0 0 24 24" fill="none" stroke="#e31e24" stroke-width="2"><rect x="4" y="3" width="16" height="18"/><path d="M9 8h2M13 8h2M9 12h2M13 12h2M10 21v-4h4v4"/></svg>
        COMMERCIAL OFFICE</div>
      <div class="type-tile">
        <svg width="12" height="12" viewBox="0 0 24 24" fill="none" stroke="#e31e24" stroke-width="2"><path d="M3 21V8l9-5 9 5v13z"/><path d="M7 21v-9h10v9M7 15h10M7 18h10"/></svg>
        INDUSTRIAL/WAREHOUSE</div>
      <div class="type-tile">
        <svg width="12" height="12" viewBox="0 0 24 24" fill="none" stroke="#e31e24" stroke-width="2"><path d="M2 12h4l3-8 4 16 3-8h6"/></svg>
        RESEARCH BIOLOGICAL LAB</div>
      <div class="type-tile">
        <svg width="12" height="12" viewBox="0 0 24 24" fill="none" stroke="#e31e24" stroke-width="2"><path d="M12 3v18M5 21h14M4 7h16M6 7l-3 7h6zM18 7l-3 7h6z"/></svg>
        ENTERPRISE RETAIL POS</div>
    </div>

    <div class="row" style="margin-top:19px"><span class="field-label">Facility size</span><span class="value">12,000 SQ FT</span></div>
    <div class="slider red"><div class="track"></div><div class="fill" style="width:27px"></div><div class="knob" style="left:22px"></div></div>

    <div class="divider" style="margin-top:17px"></div>
    <div class="field-label" style="margin-top:12px">Low voltage node drops</div>

    <div class="row" style="margin-top:12px"><span class="node-label"><i style="background:var(--red)"></i>WORKSTATION DROPS (CAT6A)</span><span class="value" style="font-size:7px">75 CABLES</span></div>
    <div class="slider red"><div class="track"></div><div class="fill" style="width:53px"></div><div class="knob" style="left:47px"></div></div>

    <div class="row" style="margin-top:14px"><span class="node-label"><i style="background:var(--ink)"></i>CEILING WAP RADIOS</span><span class="value" style="font-size:7px">8 APS</span></div>
    <div class="slider dark"><div class="track"></div><div class="fill" style="width:74px"></div><div class="knob" style="left:68px"></div></div>

    <div class="row" style="margin-top:14px"><span class="node-label"><i style="background:#555"></i>4K IP DOME CAMERAS</span><span class="value" style="font-size:7px">12 SECURITY CAMS</span></div>
    <div class="slider dark"><div class="track"></div><div class="fill" style="width:74px;background:#444"></div><div class="knob" style="left:69px;background:#444"></div></div>

    <div class="row" style="margin-top:14px"><span class="node-label"><i style="background:var(--ink)"></i>ACCESS CONTROLLED DOORS</span><span class="value" style="font-size:7px">6 BADGED DOORS</span></div>
    <div class="slider dark"><div class="track"></div><div class="fill" style="width:74px"></div><div class="knob" style="left:69px"></div></div>

    <div class="divider" style="margin-top:20px"></div>
    <div class="check" style="margin-top:11px"><span class="box on"><svg width="7" height="7" viewBox="0 0 24 24" fill="none" stroke="#fff" stroke-width="4"><path d="M4 12l5 5L20 6"/></svg></span>OPTICAL FIBER BACKBONE LINKS (MULTI-MODE OM4)</div>
    <div class="check" style="margin-top:9px"><span class="box"></span>ADD COMMERCIAL ORBITLINK FAILOVER REDUNDANCY</div>

    <div class="field-label" style="margin-top:26px">Trace code compliance standards</div>
    <div class="select">Standard Commercial - Plenum NEC Fire rated jackets
      <svg width="8" height="8" viewBox="0 0 24 24" fill="none" stroke="#111" stroke-width="3"><path d="M5 9l7 7 7-7"/></svg></div>
  </section>

  <section class="card topology">
    <div class="panel-head">
      <span class="live"><i></i>LIVE CABLING TOPOLOGY PREVIEW</span>
      <span class="grid-tag">GRID: 5M² UNITS</span>
    </div>
    <div class="plan-frame">
      <div class="plan-area" role="img" aria-label="Floor plan blueprint showing cabling topology from the central MDF server room to workstation drops, wireless access points, cameras and access-controlled doors"></div>
      <span class="model-tag">MODEL PREVIEW</span>
    </div>
    <div class="legend">
      <span><i style="background:var(--red)"></i>WORKSTATION COPPER DROPS<br>(CAT6A)</span>
      <span><i style="background:var(--ink)"></i>WAP ENTERPRISE DUAL-RADIOS</span>
      <span><i style="background:#555"></i>4K DOME CCTV SMART CAMERAS</span>
      <span><i style="background:var(--ink)"></i>RFID LOCKED ACCESS DOORS</span>
    </div>
    <div class="legend-mdf"><i></i>CENTRAL DISTRIBUTION MDF CABINET (CORE SWITCH)</div>
  </section>

  <section class="card quality">
    <h3>QUALITY AND COMPLIANCE CHECK</h3>
    <p>- All cable feeds utilize solid copper, not CCA (copper clad aluminum).</p>
    <p>- High-speed backbone spans are terminated and fusion sliced at less than 0.02dB loss coefficients.</p>
    <p>- 100% of physical nodes undergo rigorous Veritest VX-8000 validation testing to ensure flawless 10Gbps connectivity.</p>
  </section>

  <section class="card estimate">
    <div class="summary-head">ESTIMATE SUMMARY</div>
    <div class="kv" style="margin-top:15px"><span class="k">ESTIMATED RATE:</span><span class="v" style="font-weight:600">$3.02 / SQ FT</span></div>
    <div class="kv" style="margin-top:15px;padding-bottom:14px;border-bottom:1px solid var(--line)"><span class="k">SOLID COPPER WIRE:</span><span class="v">~18 SPOOLS</span></div>
    <div class="kv cost" style="margin-top:10px"><span class="k">HARDWARE/EQUIPMENT:</span><span class="v">$25,255</span></div>
    <div class="kv cost" style="margin-top:8px"><span class="k">LABOR/INSTALL:</span><span class="v">$11,005</span></div>
    <div class="kv cost fiber" style="margin-top:8px;padding-bottom:11px;border-bottom:1px solid var(--line)"><span class="k">FIBER OPTIC BACKLINK:</span><span class="v">INCLUDED</span></div>
    <div class="budget">
      <small>BUDGET PROPOSAL ESTIMATE</small>
      <strong>$36,260</strong>
      <em>INCLUDES VERITEST COMPLIANCE CERTIFICATES</em>
    </div>
    <div class="btn-primary">
      <svg width="9" height="9" viewBox="0 0 24 24" fill="none" stroke="#fff" stroke-width="2.2"><path d="M22 2L11 13M22 2l-7 20-4-9-9-4z"/></svg>
      SUBMIT CONCEPT FOR OFFICIAL BID</div>
    <div class="btn-outline">
      <svg width="9" height="9" viewBox="0 0 24 24" fill="none" stroke="#e31e24" stroke-width="2.4"><path d="M12 3v12M7 10l5 5 5-5M4 20h16"/></svg>
      PROPOSAL OUTLINE</div>
  </section>

  <section class="card support">
    <h3>NEED ARCHITECTURAL SUPPORT?</h3>
    <p>Our technicians can design custom floorplans on CAD, cooperate with local architectural partners, and assist with complex outdoor conduit pathways. Contact our main office in Virginia or Maryland for consulting support.</p>
  </section>
</main>

<section class="certs">
  <h2><svg width="9" height="10" viewBox="0 0 24 24" fill="none" stroke="#e31e24" stroke-width="2.4"><circle cx="12" cy="8" r="6"/><path d="M8.5 13L7 22l5-3 5 3-1.5-9"/></svg>PROFESSIONAL CERTIFICATIONS &amp; STANDARDS</h2>
  <p>OUR TEAMS MAINTAIN ACTIVE TRAINING CREDENTIALS FOR HIGH PERFORMANCE.</p>
  <div class="badges">
    <span class="badge"><i></i>CSDA REGISTERED</span>
    <span class="badge"><i></i>VERITEST VX-8000</span>
    <span class="badge"><i></i>OPTIC FIBER GUILD</span>
    <span class="badge"><i></i>NDAA CHIP SECURE</span>
  </div>
</section>

<div class="footer-rule" style="top:924px"></div>

<div class="foot-brand"><i></i>Wirenexa</div>
<p class="foot-about">For three decades, Wirenexa has deployed robust, clean, high-performance low voltage cabling nodes, multimode optical fibers, CCTV remote surveillance loops, and biometric security systems across Virginia and Maryland.</p>
<div class="anniv">SINCE 1996 • 30 YEARS ANNIVERSARY</div>

<div class="foot-col" style="left:324px">
  <h4>CORPORATE DIRECTORY</h4>
  <ul class="links">
    <li>→ COMMERCIAL HOME</li><li>→ OUR SERVICES</li><li>→ PROJECT PORTFOLIO</li><li>→ ESTIMATE PLANNER</li><li>→ CLOSET MONITORING</li><li>→ ABOUT US</li><li>→ CONTACT US</li>
  </ul>
</div>

<div class="foot-col" style="left:556px">
  <h4>REGIONAL OFFICES</h4>
  <div class="office" style="padding-bottom:10px;border-bottom:1px solid var(--line)">
    <b>[A] VIRGINIA HEAD OFFICES:</b>
    <div class="pin"><svg width="8" height="9" viewBox="0 0 24 24" fill="none" stroke="#e31e24" stroke-width="2.4"><path d="M12 22s-7-7-7-12a7 7 0 0 1 14 0c0 5-7 12-7 12z"/><circle cx="12" cy="10" r="2.5"/></svg><span>4410 Cedar Ridge Rd, Suite 250<br>Fairview, VA 22100</span></div>
  </div>
  <div class="office">
    <b>[B] MARYLAND BRANCH OFFICE:</b>
    <div class="pin"><svg width="8" height="9" viewBox="0 0 24 24" fill="none" stroke="#e31e24" stroke-width="2.4"><path d="M12 22s-7-7-7-12a7 7 0 0 1 14 0c0 5-7 12-7 12z"/><circle cx="12" cy="10" r="2.5"/></svg><span>2185 Harbor Point Dr Suite 400<br>Lakeside, MD 20800</span></div>
  </div>
</div>

<div class="foot-col" style="left:789px">
  <h4>INQUIRIES</h4>
  <div class="dispatch">24/7 CLIENT DISPATCH ACTIVE.</div>
  <div class="phone-bar"><svg width="10" height="10" viewBox="0 0 24 24" fill="none" stroke="#e31e24" stroke-width="2.2"><path d="M22 16.9v3a2 2 0 0 1-2.2 2 19.8 19.8 0 0 1-8.6-3.1 19.5 19.5 0 0 1-6-6A19.8 19.8 0 0 1 2.1 4.2 2 2 0 0 1 4.1 2h3a2 2 0 0 1 2 1.7c.1.9.4 1.8.7 2.7a2 2 0 0 1-.5 2.1L8 9.8a16 16 0 0 0 6 6l1.3-1.3a2 2 0 0 1 2.1-.5c.9.3 1.8.6 2.7.7a2 2 0 0 1 1.7 2z"/></svg>(888) 555-0142</div>
  <div class="mail"><svg width="10" height="8" viewBox="0 0 24 18" fill="none" stroke="#e31e24" stroke-width="2.2"><rect x="1" y="1" width="22" height="16"/><path d="M1 2l11 8 11-8"/></svg>sales@wirenexa.com</div>
  <div class="dispatch" style="margin-top:19px">FOLLOW OUR DEPLOYMENTS:</div>
  <div class="social"><span><i></i></span><span><i></i></span></div>
</div>

<div class="footer-rule" style="top:1127px"></div>
<div class="copyright">© 2026 Wirenexa LLC. All Rights Reserved. Fully Insured and Bonded Low Voltage Contractor.</div>
<div class="legal"><span>Privacy Policy</span><span>•</span><span>PCI-DSS Segregation Policy</span><span>•</span><span>CSDA Layout Code</span></div>

</body>
</html>
```